Butcher shop

We have 2 butcher shops:

Shop 9, Ridgeway Court, Aberdeen NSW 2336
Ph 02 6512 3840

47 Marlow St, Scone NSW 2337
Ph 02 6518 2274

ABN 48 907 215 816

I would like this info on reverse of card and my personal info on front of card. I have a logo I would like to use also. Require a very smooth thick matte card, with colour both sides.

Front of card should say:

Linda Farrugia
Accounts

Ph 0437 620 915
E lindafarrugia@quollmail.com.au

Industry/Entity Type

Shop

Contact Information for Business Card

Linda Farrugia
Ph 0437 620 915

Logo Text

Farrugia's Quality Meats

Logo styles of interest
Pictorial/Combination Logo
Requirements
Must have
• We use Century Gothic Font

```html
<!DOCTYPE html>
<html lang="en">
<head>
<meta charset="utf-8">
<title>Farrugia's Quality Meats – Business Card Front</title>
<link rel="stylesheet" href="https://fonts.googleapis.com/css2?family=Didact+Gothic&display=swap">
<style>
  :root {
    --card-red-centre: #9c0303;
    --card-red-mid: #7a0101;
    --card-red-edge: #560000;
    --ink-white: #ffffff;
    --mark-tone: rgba(255, 255, 255, 0.92);
    --mark-tone-soft: rgba(255, 255, 255, 0.78);
  }

  html, body {
    margin: 0;
    padding: 0;
    width: 1200px;
    height: 693px;
    overflow: hidden;
    background: var(--card-red-edge);
  }

  .business-card {
    position: relative;
    width: 1200px;
    height: 693px;
    overflow: hidden;
    background: radial-gradient(ellipse 75% 85% at 50% 62%,
      var(--card-red-centre) 0%,
      var(--card-red-mid) 45%,
      var(--card-red-edge) 100%);
    font-family: "Didact Gothic", "Century Gothic", sans-serif;
    color: var(--ink-white);
  }

  .brand-illustration {
    position: absolute;
    left: 384px;
    top: 82px;
    width: 432px;
    height: 232px;
    border-radius: 18px 28px 6px 6px;
    background: linear-gradient(180deg, var(--mark-tone) 0%, var(--mark-tone-soft) 100%);
  }

  .horizon-arc {
    position: absolute;
    left: 0;
    top: 290px;
    width: 1200px;
    height: 60px;
  }

  .brand-name {
    position: absolute;
    left: 0;
    width: 1200px;
    top: 338px;
    margin: 0;
    text-align: center;
    font-size: 88px;
    font-weight: 400;
    line-height: 1;
    letter-spacing: 3px;
    white-space: nowrap;
  }

  .contact-person,
  .contact-details {
    position: absolute;
    top: 556px;
    margin: 0;
    font-size: 42px;
    line-height: 49px;
    font-weight: 400;
    letter-spacing: 1.5px;
    white-space: nowrap;
  }

  .contact-person { left: 47px; }
  .contact-details { right: 51px; text-align: right; }

  .contact-person span,
  .contact-details span { display: block; }
</style>
</head>
<body>
  <main class="business-card">
    <div class="brand-illustration" role="img" aria-label="Placeholder area reserved for the shop's pictorial brand mark"></div>

    <svg class="horizon-arc" viewBox="0 0 1200 60" aria-hidden="true">
      <defs>
        <linearGradient id="arcFade" x1="0" y1="0" x2="1" y2="0">
          <stop offset="0" stop-color="#ffffff" stop-opacity="0"/>
          <stop offset="0.3" stop-color="#ffffff" stop-opacity="0.9"/>
          <stop offset="0.6" stop-color="#ffffff" stop-opacity="1"/>
          <stop offset="1" stop-color="#ffffff" stop-opacity="0"/>
        </linearGradient>
      </defs>
      <path d="M305 46 Q700 2 1085 50" fill="none" stroke="url(#arcFade)" stroke-width="3"/>
    </svg>

    <h1 class="brand-name">Farrugia’s Quality Meats</h1>

    <p class="contact-person">
      <span class="person-name">Linda Farrugia</span>
      <span class="person-role">Accounts</span>
    </p>

    <p class="contact-details">
      <span class="contact-phone">Ph 0437 620 915</span>
      <span class="contact-email">E lindafarrugia@quollmail.com.au</span>
    </p>
  </main>
</body>
</html>
```